Inspiring Wordpress Design for Brightpath Figure Renewal: Assured Contest

We need a web design for a medical weight loss clinic near San Francisco. We would like for our site to be similar to http://www.trimlarkhaven.com:

The winning design will communicate a youthful, energetic, and fun vibe. We want to imply success and vitality in contrast to the guilt, shame, and burden of traditional weight loss. At the same time, it is a very scientifically oriented and physician supervised so we need it to convey authority and science at the same time.

Our logo and font files are attached.

Target Demographic: 30-50 year old women of White, Asian, Latin, and African American Backgrounds. Income $35-120k.

Target Market(s)

We are a medical Weight Loss Center. Our target audience is women aged 30-55 in low middle to middle class, incomes from $30k to $150k per year. Target Audience is of mixed race including white, Latin, African American and Asian.

Industry/Entity Type

Clinic

Font styles to use
Other font styles liked:
• 738162 Acrom Family (OTF) $160.00 The Velvet Quarry Ltd package Desktop users: 10 - 915374 Twentieth Century 1 Volume (OTF) $157.00 Glyphorra package Desktop users: 5 - 608293 Twentieth Century 2 Volume (Win TTF) $105.00 Glyphorra package

Requirements
Must have
• Tabs:
Science of Weight Loss Success
Success Stories
Location and Hours
Contact Us
Espanol

Need an Area for Our Slogan ( exact slogan TBD)

Please include Stock Images and links to those images in your design.

We would Like to Include Three Buttons in the design:
1. Stop the Low Calorie Starvation Diet
2. Why Coral Bayslim
3. Become a Skinny Fat Burner Today
Nice to have
• Fonts that we have purchased are attached. Please use these.

```html
<!DOCTYPE html>
<html lang="en">
<head>
<meta charset="utf-8">
<title>Coral Bayslim – Medical Weight Loss Centers</title>
<link href="https://fonts.googleapis.com/css2?family=Jost:ital,wght@0,400;0,500;0,600;0,700;1,400&family=Questrial&display=swap" rel="stylesheet">
<style>
:root{
  --teal:#4fb3ae;
  --teal-dark:#2a8783;
  --teal-text:#1f8a84;
  --ink-teal:#16625e;
  --yellow:#f5b800;
  --grey-head:#666a6b;
  --grey-body:#7b7f80;
  --dark:#333;
  --white:#fff;
}
*{margin:0;padding:0;box-sizing:border-box}
html,body{width:807px;height:1200px;overflow:hidden;background:var(--white)}
body{position:relative;font-family:"Questrial",sans-serif;color:var(--grey-body)}
.abs{position:absolute}
.top-rule{left:0;top:0;width:807px;height:3px;background:var(--teal)}
.brand{left:62px;top:18px}
.brand-name{font-family:"Jost",sans-serif;font-weight:500;font-size:27px;color:var(--yellow);line-height:1;letter-spacing:.3px}
.brand-tag{font-family:"Jost",sans-serif;font-size:7.5px;letter-spacing:2.3px;color:var(--teal-dark);margin-top:4px}
.callback{left:580px;top:25px;font-size:9px;line-height:13px;color:#555}
.phone-icon{left:716px;top:22px}
.nav{left:62px;top:78px;width:683px;height:39px;background:var(--teal);display:flex}
.nav a{color:var(--white);text-decoration:none;font-size:9px;display:flex;align-items:center;justify-content:center;border-right:1px solid rgba(255,255,255,.25);height:100%}
.nav a:last-child{border-right:0}
.nav .active{background:var(--yellow)}
.hero{left:62px;top:117px;width:683px;height:336px;background:linear-gradient(90deg,#e9ebe6 0%,#f4f4f1 35%,#eef3ea 60%,#dfe9d5 85%,#e8efe1 100%)}
.hero-photo{left:62px;top:117px;width:340px;height:336px;background:radial-gradient(ellipse at 45% 45%,#f0d9c8 0%,#ead2bf 35%,rgba(240,238,232,0) 72%)}
.hero-kicker{left:406px;top:215px;font-family:"Jost",sans-serif;font-weight:500;font-size:20px;color:var(--ink-teal)}
.hero-title{left:406px;top:234px;font-family:"Jost",sans-serif;font-weight:700;font-size:31px;color:var(--yellow)}
.hero-sub{left:410px;top:281px;font-family:"Jost",sans-serif;font-size:15px;color:#333}
.price{left:421px;top:314px;font-family:"Jost",sans-serif;font-weight:600;font-size:32px;color:#333;line-height:1}
.price small{font-size:14px;font-weight:500}
.btn-start{left:566px;top:317px;width:133px;height:38px;background:var(--teal);color:var(--white);font-family:"Jost",sans-serif;font-weight:500;font-size:12px;letter-spacing:.5px;display:flex;align-items:center;justify-content:center}
.slide-arrow{top:273px;width:31px;height:32px;background:var(--white);display:flex;align-items:center;justify-content:center}
.slide-arrow.left{left:48px}
.slide-arrow.right{left:729px}
.feature{top:457px;width:223px;height:123px;color:var(--white);padding:18px 16px}
.feature h2{font-family:"Jost",sans-serif;font-weight:600;font-size:20px;line-height:25px}
.feature p{font-size:7.5px;line-height:12px;margin-top:18px}
.f1{left:65px;background:var(--teal)}
.f2{left:292px;background:var(--teal-dark)}
.f3{left:519px;background:var(--yellow)}
.section-title{font-family:"Jost",sans-serif;font-weight:600;font-size:20px;color:var(--grey-head)}
.apple-photo{left:0;top:640px;width:245px;height:152px;background:radial-gradient(ellipse at 60% 45%,#a5cf5a 0%,#c7e19a 30%,rgba(255,255,255,0) 70%)}
.lead{font-family:"Jost",sans-serif;font-size:12.5px;line-height:17px;color:var(--teal-text)}
.body{font-size:8.5px;line-height:13.5px;color:var(--grey-body)}
.star-box{left:548px;width:40px;height:40px;background:#eeeeee;box-shadow:0 2px 3px rgba(0,0,0,.2);display:flex;align-items:center;justify-content:center}
.review-text{left:603px;width:145px;font-size:10px;line-height:15px;color:var(--teal-text)}
.divider{left:62px;top:805px;width:683px;height:1px;background:#e6e6e6}
.story-photo{left:62px;top:880px;width:202px;height:118px;background:linear-gradient(90deg,#dfe3e6,#b9c0c6 45%,#e8ebec 80%,#cfd8d4)}
.mini-arrow{top:930px;width:16px;height:18px;background:rgba(255,255,255,.85);font-size:9px;display:flex;align-items:center;justify-content:center;color:#888}
.news-rule{left:308px;top:998px;width:192px;height:1px;background:#e4e4e4}
.btn-more{left:308px;top:1019px;width:77px;height:29px;background:var(--yellow);color:var(--white);font-family:"Jost",sans-serif;font-weight:600;font-size:10px;display:flex;align-items:center;justify-content:center}
.quote{left:548px;top:877px;width:200px;font-family:"Jost",sans-serif;font-style:italic;font-size:10px;line-height:15px;color:var(--teal-text)}
.quote-author{left:548px;top:967px;font-size:8px;color:#555}
.quote-nav{left:549px;top:993px;width:50px;height:24px;background:#eee;border-radius:3px;box-shadow:0 2px 3px rgba(0,0,0,.25);display:flex}
.quote-nav span{flex:1;display:flex;align-items:center;justify-content:center;font-size:8px;color:#444}
.quote-nav span:first-child{border-right:1px solid #d5d5d5}
.footer{left:0;top:1092px;width:807px;height:108px;background:var(--teal)}
.social{left:288px;top:1109px;display:flex;gap:7px}
.social span{width:27px;height:27px;border-radius:50%;background:var(--white)}
.social span:first-child{background:#2e7f7b}
.footer-links{left:0;top:1154px;width:807px;text-align:center;font-size:9.5px;color:var(--white)}
.footer-links span{margin:0 5px}
.copyright{left:0;top:1171px;width:807px;text-align:center;font-size:7.5px;color:var(--white)}
</style>
</head>
<body>
<div class="abs top-rule"></div>

<div class="abs brand">
  <div class="brand-name">Coral Bayslim</div>
  <div class="brand-tag">MEDICAL WEIGHT LOSS CENTERS</div>
</div>

<div class="abs callback">FREE INSTANT CALL BACK<br>OR CALL: 1 - 800 - 555 - 27 - 84</div>
<svg class="abs phone-icon" width="28" height="28" viewBox="0 0 28 28" aria-label="Phone">
  <path d="M4 11c0-4 4-6 10-6s10 2 10 6l-4 1-1-3c-3-1-7-1-10 0l-1 3z" fill="var(--yellow)"/>
  <path d="M7 14h14l3 9H4z" fill="var(--yellow)"/>
  <circle cx="14" cy="18" r="3" fill="var(--white)"/>
</svg>

<nav class="abs nav">
  <a class="active" style="width:77px">HOME</a>
  <a style="width:207px">SCIENCE OF WEIGHT LOSS SUCCESS</a>
  <a style="width:132px">SUCCESS STORIES</a>
  <a style="width:157px">LOCATION AND HOURS</a>
  <a style="width:110px">CONTACT US</a>
</nav>

<div class="abs hero" role="img" aria-label="Photo of a smiling woman measuring her waist with a tape measure"></div>
<div class="abs hero-photo"></div>
<div class="abs hero-kicker">MEDICAL WEIGHT LOSS CLINIC</div>
<div class="abs hero-title">in San Francisco</div>
<div class="abs hero-sub">Donec accumsan malesuada orcionecs</div>
<div class="abs price">$100<small>/Month</small></div>
<div class="abs btn-start">GET STARTED</div>
<div class="abs slide-arrow left"><svg width="8" height="14" viewBox="0 0 8 14"><path d="M7 1 1 7l6 6" fill="none" stroke="#888" stroke-width="1.2"/></svg></div>
<div class="abs slide-arrow right"><svg width="8" height="14" viewBox="0 0 8 14"><path d="M1 1l6 6-6 6" fill="none" stroke="#888" stroke-width="1.2"/></svg></div>

<div class="abs feature f1"><h2>Stop the Low Calorie Starvation Diet</h2><p>Lorem ipsum dolor sit amet, consectetueradipiscing elit auris vel tortorvitae nibh.</p></div>
<div class="abs feature f2"><h2>Why Coral<br>Bayslim</h2><p>Lorem ipsum dolor sit amet, consectetueradipiscing elit auris vel tortorvitae nibh.</p></div>
<div class="abs feature f3"><h2>Become a Skinny Fat Burner Today</h2><p>Lorem ipsum dolor sit amet, consectetueradipiscing elit auris vel tortorvitae nibh.</p></div>

<h2 class="abs section-title" style="left:63px;top:606px">Welcome to Coral Bayslim</h2>
<div class="abs apple-photo" role="img" aria-label="Photo of a green apple wrapped in a measuring tape"></div>
<p class="abs lead" style="left:258px;top:663px;width:250px">Lorem ipsum dolor sit amet, consectetueradipi-scing elit auris vel tortorvitae nibh.</p>
<p class="abs body" style="left:258px;top:713px;width:250px">Praesent vestibulum molestie lacus. Aenean nonummy hendrerit mauris. Phasellus porta. Fusce suscipit varius mi.Cum sociis natoque penatibus et magnis dis parturient montes, nascetur ridiculus musaulla dui.</p>

<h2 class="abs section-title" style="left:546px;top:606px">Review Us</h2>
<div class="abs star-box" style="top:653px"><svg width="14" height="14" viewBox="0 0 24 24"><path d="M12 2l3 7 7 .6-5.4 4.7 1.7 7.2L12 17.8 5.7 21.5l1.7-7.2L2 9.6 9 9z" fill="#666"/></svg></div>
<p class="abs review-text" style="top:658px">Lorem ipsum dolor sit amet, con-sectetueradipiscing elit auri</p>
<div class="abs star-box" style="top:715px"><svg width="14" height="14" viewBox="0 0 24 24"><path d="M12 2l3 7 7 .6-5.4 4.7 1.7 7.2L12 17.8 5.7 21.5l1.7-7.2L2 9.6 9 9z" fill="#666"/></svg></div>
<p class="abs review-text" style="top:720px">Lorem ipsum dolor sit amet, con-sectetueradipiscing elit auri</p>

<div class="abs divider"></div>

<h2 class="abs section-title" style="left:62px;top:830px">Success Stories</h2>
<div class="abs story-photo" role="img" aria-label="Photo of a slim woman measuring her waist"></div>
<div class="abs mini-arrow" style="left:62px">‹</div>
<div class="abs mini-arrow" style="left:248px">›</div>
<p class="abs body" style="left:62px;top:1014px;width:205px;font-size:8px;line-height:12px">Praesent vestibulum molestie lacus. Aenean nonummy hendrerit mauris. Phasellus porta. Fusce suscipit .et magnis dis parturient montes ur ridiculus mus</p>

<h2 class="abs section-title" style="left:308px;top:830px">Weight loss News</h2>
<p class="abs body" style="left:308px;top:876px;font-size:8px">03/11/2014</p>
<p class="abs lead" style="left:308px;top:896px;width:205px;font-size:10px;line-height:15px">Lorem ipsum dolor sit amet, consectetueradipi-scing elit auris vel tortorvitae nibh.</p>
<p class="abs body" style="left:308px;top:942px;width:205px;font-size:7.5px;line-height:12px">Praesent vestibulum molestie lacus. Aenean nonummy hendrerit mauris. Phasellus porta. Fusce suscipit .et magnis dis parturient montes ur ridiculus mus</p>
<div class="abs news-rule"></div>
<div class="abs btn-more">Read More</div>

<h2 class="abs section-title" style="left:548px;top:830px">Testimonials</h2>
<p class="abs quote">I am so happy. I will recommend this clinic to whoever wants to lose weight. It has changed my life significantly. Taking the medication reminds me to eat a healthy balanced diet. I also exercise.</p>
<p class="abs quote-author">Dana - age 41 lost 18 pounds</p>
<div class="abs quote-nav"><span>←</span><span>→</span></div>

<footer class="abs footer"></footer>
<div class="abs social"><span></span><span></span><span></span><span></span><span></span><span></span><span></span></div>
<div class="abs footer-links"><span>Weight Loss Program</span><span>Tips &amp; Tools</span><span>Testimonials</span><span>Contact &amp; Hours</span><span>Privacy Policy</span><span>Careers</span><span>Español</span></div>
<div class="abs copyright">© 2014 Coral Bayslim all rights reserved privacy policy &nbsp;|&nbsp; Terms and conditions</div>
</body>
</html>
```